Letterhead, stationery and email signature for construction business

I need the letterhead, stationery and email signature designs for a construction business. I want them to have a corporate feel to them.

I've attached the logo for reference.

```html
<!DOCTYPE html>
<html lang="en">
<head>
<meta charset="utf-8">
<title>Harlow Build – Letterhead</title>
<link rel="stylesheet" href="https://fonts.googleapis.com/css2?family=Lato:wght@400;700&family=Open+Sans:wght@400&family=Italianno&display=swap">
<style>
  :root {
    --backdrop: #e3e3e3;
    --paper: #ffffff;
    --brand-blue: #2b5aa8;
    --rule-blue: #2a5db0;
    --ink: #1b1b1b;
    --contact-ink: #2a2a2a;
  }
  * { box-sizing: border-box; margin: 0; padding: 0; }
  html, body {
    width: 1200px; height: 1141px; overflow: hidden;
    background: var(--backdrop);
  }
  .letterhead {
    position: absolute; left: 211px; top: 20px;
    width: 778px; height: 1100px;
    background: var(--paper);
    box-shadow: 0 2px 10px rgba(0,0,0,0.18);
    font-family: 'Lato', sans-serif;
    color: var(--ink);
  }
  .brand {
    position: absolute; left: 39px; top: 72px;
    display: flex; align-items: center; gap: 14px;
  }
  .brand-square { width: 62px; height: 62px; background: var(--brand-blue); }
  .brand-name {
    font-family: 'Lato', sans-serif; font-weight: 700;
    font-size: 38px; letter-spacing: 0.5px; color: var(--brand-blue);
    line-height: 1;
  }
  .header-divider {
    position: absolute; left: 509px; top: 45px;
    width: 2px; height: 111px; background: var(--rule-blue);
  }
  .contact {
    position: absolute; left: 539px; top: 38px;
    font-family: 'Open Sans', sans-serif; font-size: 16.5px;
    color: var(--contact-ink); line-height: 22px;
  }
  .contact .address { margin-bottom: 8px; }
  .contact-row { display: flex; align-items: center; gap: 6px; }
  .contact-row svg { width: 13px; height: 13px; flex: none; fill: var(--brand-blue); }
  .header-rule {
    position: absolute; left: 39px; top: 194px;
    width: 700px; height: 2px; background: var(--rule-blue);
  }
  .letter-body {
    position: absolute; left: 39px; top: 252px; width: 700px;
    font-size: 15px; line-height: 18.4px;
  }
  .letter-date { line-height: 20px; }
  .recipient { margin-top: 18px; }
  .recipient-company { margin-top: 17px; }
  .salutation {
    margin-top: 20px; font-size: 18.5px; font-weight: 700; line-height: 22px;
  }
  .letter-text { margin-top: 19px; }
  .letter-text p {
    font-size: 14.6px; line-height: 17.2px; text-align: justify;
    margin-bottom: 16px;
  }
  .closing { margin-top: 28px; }
  .signature {
    margin-top: 70px; font-family: 'Italianno', cursive;
    font-size: 40px; line-height: 40px; color: #111;
  }
</style>
</head>
<body>
<main class="letterhead">
  <header>
    <div class="brand">
      <span class="brand-square"></span>
      <span class="brand-name">HARLOW BUILD</span>
    </div>
    <div class="header-divider"></div>
    <address class="contact" style="font-style:normal">
      <div class="address">Your address, City<br>State, Zip 1234</div>
      <div class="contact-row">
        <svg viewBox="0 0 16 16"><path d="M2 6c0-2 2.5-3.5 6-3.5S14 4 14 6v1h-3V5.5H5V7H2z M4 8h8l2 5H2z"/></svg>
        <span>123 456 789</span>
      </div>
      <div class="contact-row">
        <svg viewBox="0 0 16 16"><path d="M1 4h14v9H1z" /><path d="M1 4l7 5 7-5" fill="none" stroke="#fff" stroke-width="1.3"/></svg>
        <span>info@yourgmail.com</span>
      </div>
      <div class="contact-row">
        <svg viewBox="0 0 16 16"><circle cx="8" cy="8" r="7"/><path d="M1 8h14M8 1c-3 3.5-3 10.5 0 14M8 1c3 3.5 3 10.5 0 14" fill="none" stroke="#fff" stroke-width="1"/></svg>
        <span>www.yourwebsite.com</span>
      </div>
    </address>
    <div class="header-rule"></div>
  </header>

  <section class="letter-body">
    <div class="letter-date">January-03-2020</div>
    <div class="recipient">Mr, Alan Reed<br>President</div>
    <div class="recipient-company">Norvale Corporation<br>123 Street Name, Suite# 10<br>City, State, 120023</div>
    <h1 class="salutation">Dear Mr, Alan</h1>
    <div class="letter-text">
      <p>Lorem ipsum dolor sit amet, consectetur adipiscing elit, sed do eiusmod tempor incididunt ut labore et dolore magna aliqua. Ut enim ad minim veniam, quis nostrud exercitation ullamco laboris nisi ut aliquip ex ea commodo consequat. Duis aute irure dolor in reprehenderit in voluptate velit esse cillum dolore eu fugiat nulla pariatur.</p>
      <p>Lorem ipsum dolor sit amet, consectetur adipiscing elit, sed do eiusmod tempor incididunt ut labore et dolore magna aliqua. Ut enim ad minim veniam, quis nostrud exercitation ullamco laboris nisi ut aliquip ex ea commodo consequat. Duis aute irure dolor in reprehenderit in voluptate velit esse cillum dolore eu fugiat nulla pariatur.</p>
      <p>Lorem ipsum dolor sit amet, consectetur adipiscing elit, sed do eiusmod tempor incididunt ut labore et dolore magna aliqua. Ut enim ad minim veniam, quis nostrud exercitation ullamco laboris nisi ut aliquip ex ea commodo consequat.</p>
      <p>Excepteur sint occaecat cupidatat non proident, sunt in culpa qui officia deserunt mollit anim id est laborum. re et dolore magnam aliquam quaerat voluptatem.</p>
    </div>
    <div class="closing">Regards</div>
    <div class="signature">Daniel Price</div>
  </section>
</main>
</body>
</html>
```